High Quality Business card for Property Management Agency - Super Classy and professional design

High Quality Business card design.

We need a business card designed for our Property Management Agency.
We are located on Sydney's Northern Beaches and manage beautiful properties along the beach and harbor.
We need a design that oozes modern, classy and professional.
I would like it to be double sided with contact details and logo on the front and just the logo on the back.

I need a print ready PDF version of the file as well as an editable photoshop (PSD) version of the file.

Logo and information details attached.

Target Market(s)

Property owners/investors, Male and Female Aged 28-65

Industry/Entity Type

Real Estate

Contact Information for Business Card

Tom Harlow
Tel: 0437 216 590
Email: tom@harlowestates.com.au
Website: www.harlowestates.com.au
Address: Level 2, 17 Kestrel Rd, Wendale NSW 2081

Font styles to use
Sans Serif

Requirements
Must have
• - Logo front and back
• - Business card details listed above and attached
• - Colour
Nice to have
• Sleek and professional

```html
<!DOCTYPE html>
<html lang="en">
<head>
<meta charset="utf-8">
<title>Harlow Estates – Business Card</title>
<link href="https://fonts.googleapis.com/css2?family=Open+Sans:wght@400;600;700&family=Roboto:wght@400;500&display=swap" rel="stylesheet">
<style>
  :root {
    --backdrop: #7a5d3f;
    --card: #16191c;
    --card-edge: #0e1012;
    --teal: #3bb6bd;
    --teal-deep: #1d8f98;
    --white: #f4f6f7;
    --muted: #d9dde0;
  }
  * { margin: 0; padding: 0; box-sizing: border-box; }
  html, body {
    width: 1200px; height: 1023px; overflow: hidden;
    background: var(--backdrop);
  }
  .sheet {
    position: relative; width: 1200px; height: 1023px;
    display: flex; flex-direction: column; align-items: center;
    justify-content: center; gap: 63px;
  }
  .card {
    position: relative; width: 700px; height: 400px;
    border-radius: 22px; overflow: hidden;
    background: radial-gradient(ellipse at 45% 40%, #1e2226 0%, var(--card) 60%, var(--card-edge) 100%);
    box-shadow: 0 14px 30px rgba(0,0,0,0.35);
  }
  .card__corners { position: absolute; inset: 0; }

  /* Back: logo only */
  .brand {
    font-family: "Open Sans", sans-serif; font-weight: 700;
    color: var(--white); text-transform: uppercase; letter-spacing: 1px;
    display: flex; align-items: center; gap: 14px;
  }
  .brand__dot {
    width: 16px; height: 16px; border-radius: 50%; background: var(--teal);
  }
  .card--back .brand {
    position: absolute; left: 50%; top: 50%;
    transform: translate(-50%, -50%); font-size: 54px; white-space: nowrap;
  }

  /* Front: details */
  .card--front .brand {
    position: absolute; right: 54px; top: 118px; font-size: 40px; white-space: nowrap;
  }
  .holder {
    position: absolute; left: 60px; top: 56px;
    font-family: "Open Sans", sans-serif; font-weight: 400;
    font-size: 30px; color: var(--teal); letter-spacing: 1px;
  }
  .contact {
    position: absolute; left: 60px; bottom: 60px; list-style: none;
    font-family: "Roboto", sans-serif; font-size: 16px; color: var(--muted);
    letter-spacing: 0.6px; line-height: 1.45;
  }
  .contact li { display: flex; align-items: flex-start; gap: 12px; }
  .contact svg { flex: none; width: 15px; height: 15px; margin-top: 3px; }
  .card__band { position: absolute; left: 0; bottom: 0; width: 100%; height: 14px; }
</style>
</head>
<body>
<main class="sheet">

  <section class="card card--back" aria-label="Card back">
    <svg class="card__corners" viewBox="0 0 700 400" aria-hidden="true">
      <polygon points="470,0 700,0 700,40" fill="var(--teal)"/>
      <polygon points="0,360 0,400 240,400" fill="var(--teal)"/>
    </svg>
    <div class="brand"><span class="brand__dot"></span>Harlow Estates</div>
  </section>

  <section class="card card--front" aria-label="Card front">
    <p class="holder">Tom Harlow</p>
    <div class="brand"><span class="brand__dot"></span>Harlow Estates</div>
    <ul class="contact">
      <li>
        <svg viewBox="0 0 16 16"><path d="M4 1.5l2.2 2.8-1.3 1.6c.9 2 2.5 3.6 4.5 4.5l1.6-1.3 2.8 2.2-1.4 2.2C7.6 13.4 2.6 8.4 1.8 3.1z" fill="var(--teal)"/></svg>
        0437 216 590
      </li>
      <li>
        <svg viewBox="0 0 16 16"><rect x="1.5" y="3.5" width="13" height="9" fill="none" stroke="var(--muted)" stroke-width="1.3"/><path d="M1.5 3.5l6.5 5 6.5-5" fill="none" stroke="var(--muted)" stroke-width="1.3"/></svg>
        tom@harlowestates.com.au
      </li>
      <li>
        <svg viewBox="0 0 16 16"><circle cx="8" cy="8" r="6.5" fill="none" stroke="var(--muted)" stroke-width="1.3"/><path d="M1.5 8h13M8 1.5c-3 3.5-3 9.5 0 13M8 1.5c3 3.5 3 9.5 0 13" fill="none" stroke="var(--muted)" stroke-width="1.1"/></svg>
        www.harlowestates.com.au
      </li>
      <li>
        <svg viewBox="0 0 16 16"><path d="M8 15s-5-5.2-5-8.8a5 5 0 0110 0C13 9.8 8 15 8 15z" fill="var(--teal)"/><circle cx="8" cy="6.3" r="1.8" fill="var(--card)"/></svg>
        <span>Level 2, 17 Kestrel Rd,<br>Wendale NSW 2081</span>
      </li>
    </ul>
    <svg class="card__band" viewBox="0 0 700 14" preserveAspectRatio="none" aria-hidden="true">
      <polygon points="0,4 300,4 312,0 700,0 700,14 0,14" fill="var(--teal-deep)"/>
    </svg>
  </section>

</main>
</body>
</html>
```